New Web Design Project

New Roofing Website homepage mockup

Complete design document here: https://files.plorvex.net/doc/7tQmZrA2kLwP9xVbN4cYhE3sJdF8gUoR6iKe1nTy/edit?usp=sharing
Updates

Number of Pages Required

1 page

Font styles to use
Sans Serif

```html
<!DOCTYPE html>
<html lang="en">
<head>
<meta charset="utf-8">
<title>Keystone Roofing – Home</title>
<link href="https://fonts.googleapis.com/css2?family=Open+Sans:wght@400;600;700;800&display=swap" rel="stylesheet">
<style>
:root{
  --blue:#29a8e0;
  --ink:#222;
  --text:#555;
  --light:#f6f6f6;
  --estimate-bg:#f1f1f1;
  --footer-bottom:#2c2f33;
  --white:#fff;
}
*{box-sizing:border-box;margin:0;padding:0}
html,body{width:1200px;height:4518px;overflow:hidden}
body{position:relative;background:var(--white);font-family:"Open Sans",Arial,sans-serif;color:var(--ink)}
.abs{position:absolute}
.ph{position:absolute}

/* hero */
.hero-photo{left:0;top:0;width:1200px;height:652px;background:linear-gradient(160deg,#6d655f 0%,#5b514b 45%,#7b6a5e 75%,#a08774 100%);clip-path:polygon(0 0,1200px 0,1200px 228px,438px 652px,0 403px)}
.hero-lines{left:0;top:0}
.topbar{top:14px;right:162px;font-size:11px;color:#fff;display:flex;gap:12px;align-items:center}
.topbar span{display:flex;align-items:center;gap:5px}
.nav{left:161px;top:47px;width:877px;height:51px;background:#fff;display:flex;align-items:center;justify-content:space-between;padding:0 22px 0 12px}
.brand{display:flex;align-items:center;gap:6px;font-size:15px;font-weight:700;color:var(--blue)}
.brand i{width:14px;height:14px;background:var(--blue);display:block}
.nav ul{list-style:none;display:flex;gap:24px;font-size:10.5px;font-weight:700;color:#333}
.hero-title{left:161px;top:182px;color:#fff;font-weight:800;font-size:74px;line-height:1;letter-spacing:1px}
.hero-sub{left:161px;top:266px;color:#fff;font-weight:700;font-size:38px;letter-spacing:1px}
.btn-estimate{left:161px;top:363px;width:210px;height:35px;background:var(--blue);color:#fff;font-size:12.5px;font-weight:600;display:flex;align-items:center;justify-content:center}
.quote-shadow{left:757px;top:160px;width:281px;height:335px;background:#4a4a4a}
.quote{left:751px;top:153px;width:276px;height:321px;background:#fff;padding:24px 18px}
.quote h3{font-size:14px;font-weight:700;text-align:center;margin-bottom:20px}
.field{height:28px;background:#eee;margin:0 3px 17px;font-size:9px;color:#aaa;padding:8px 11px}
.field.msg{height:52px}
.send{width:112px;height:28px;background:var(--blue);color:#fff;font-size:10px;font-weight:700;display:flex;align-items:center;justify-content:center;margin:0 auto}

.section-title{width:1200px;left:0;text-align:center;font-weight:700;color:var(--ink)}

/* services */
.service{top:860px;width:428px;height:459px;border-radius:4px;overflow:hidden}
.service .label{position:absolute;bottom:28px;width:100%;text-align:center;color:#fff;font-size:22px;font-weight:700;letter-spacing:1px}
.band{left:0;top:1394px;width:1200px;height:415px;background:var(--blue)}
.hex{top:1466px;width:274px;height:239px;clip-path:polygon(25% 0,75% 0,100% 50%,75% 100%,25% 100%,0 50%)}
.hex-label{top:1722px;width:300px;text-align:center;color:#fff;font-size:13.5px;font-weight:700}

/* about */
.about-bg{left:0;top:1809px;width:1200px;height:468px;background:var(--light)}
.about-title{left:158px;top:1864px;font-size:29px;font-weight:600}
.about-text{left:161px;top:1925px;width:386px;font-size:19.5px;line-height:32px;text-align:justify;color:#333;hyphens:auto;-webkit-hyphens:auto}

/* roofs */
.roof{top:2428px;width:264px;height:238px;background:#fff;box-shadow:0 0 0 1px #ececec}
.roof .img{height:203px}
.roof .name{text-align:center;font-size:12px;font-weight:700;margin-top:10px}

/* projects */
.project-label{left:96px;top:3212px;color:#fff;font-size:22px}

/* estimate */
.estimate-bg{left:0;top:3329px;width:1200px;height:539px;background:var(--estimate-bg)}
.step{top:3419px;display:flex;align-items:center;gap:16px;font-size:11.5px;color:#555}
.step b{width:30px;height:30px;border-radius:50%;background:#666;color:#fff;display:flex;align-items:center;justify-content:center;font-size:10px;font-weight:400}
.step.active{color:var(--blue)}
.step.active b{background:var(--blue)}
.product{top:3536px;width:205px;height:279px;background:#fff;overflow:hidden}
.product .img{height:158px;position:relative}
.product .price{position:absolute;left:12px;top:12px;background:var(--blue);color:#fff;font-size:11px;padding:3px 9px}
.product h4{font-size:12px;font-weight:600;margin:9px 0 0 14px;white-space:nowrap}
.product .tier{font-size:8.5px;color:#999;margin-left:14px;height:12px}
.product .info{font-size:10px;color:var(--blue);margin:8px 0 0 16px;text-decoration:underline}
.product .calc{margin:14px 0 0 14px;width:146px;height:22px;border-radius:11px;background:#222;color:#fff;font-size:9.5px;display:flex;align-items:center;justify-content:center}
.product .calc.on{background:var(--blue)}

/* testimonial */
.quote-text{left:158px;top:3968px;width:884px;text-align:center;font-size:13.5px;line-height:22.5px;color:#666}
.avatar{left:563px;top:4077px;width:70px;height:70px;border-radius:50%;border:3px solid #ddd}
.client{left:0;width:1200px;text-align:center}

/* footer */
.footer{left:0;top:4259px;width:1200px;height:223px;background:var(--blue)}
.fcol{top:4302px;color:#fff}
.fcol h5{font-size:15px;font-weight:400;margin-bottom:20px}
.fcol ul{list-style:none;font-size:11.5px;line-height:26px}
.fcol ul li::before{content:"";display:inline-block;width:5px;height:5px;background:#fff;border-radius:50%;margin-right:8px;vertical-align:middle}
.fcol p{font-size:10.5px;line-height:16px;width:165px}
.contact li{display:flex;align-items:center;gap:12px;margin-bottom:8px}
.contact li::before{display:none!important}
.copy{left:0;top:4482px;width:1200px;height:36px;background:var(--footer-bottom);color:#ccc;font-size:11px;display:flex;align-items:center;justify-content:space-between;padding:0 162px}
</style>
</head>
<body>

<!-- HERO -->
<div class="ph hero-photo" role="img" aria-label="Photo of a Victorian house roofline with gables and chimneys"></div>
<svg class="abs hero-lines" width="1200" height="760" viewBox="0 0 1200 760">
  <g stroke="#29a8e0" stroke-width="1.2" fill="none">
    <line x1="40" y1="580" x2="300" y2="465"/>
    <line x1="400" y1="714" x2="760" y2="520"/>
    <line x1="581" y1="712" x2="1200" y2="380"/>
    <line x1="820" y1="500" x2="1200" y2="290"/>
  </g>
  <g fill="#29a8e0">
    <polygon points="126,548 133,552 133,560 126,564 119,560 119,552"/>
    <polygon points="631,599 638,603 638,611 631,615 624,611 624,603"/>
    <polygon points="400,708 405,711 405,717 400,720 395,717 395,711"/>
    <polygon points="581,703 589,707 589,717 581,721 573,717 573,707"/>
  </g>
</svg>

<div class="abs topbar">
  <span><svg width="10" height="10" viewBox="0 0 24 24"><path fill="#fff" d="M6.6 10.8a15 15 0 0 0 6.6 6.6l2.2-2.2c.3-.3.7-.4 1-.2 1.1.4 2.3.6 3.6.6.6 0 1 .4 1 1V20c0 .6-.4 1-1 1A17 17 0 0 1 3 4c0-.6.4-1 1-1h3.5c.6 0 1 .4 1 1 0 1.3.2 2.5.6 3.6.1.3 0 .7-.2 1z"/></svg>555-014-2290</span>
  <span>|</span>
  <span><svg width="11" height="9" viewBox="0 0 22 16"><rect x="1" y="1" width="20" height="14" fill="none" stroke="#fff" stroke-width="2"/><path d="M1 1l10 8 10-8" fill="none" stroke="#fff" stroke-width="2"/></svg>evan@keystoneroofingco.com</span>
</div>

<header class="abs nav">
  <div class="brand"><i></i>KEYSTONE ROOFING</div>
  <ul><li>KEYSTONE ROOFING</li><li>BLOG</li><li>REVIEWS</li><li>ABOUT</li><li>SERVICES</li><li>AFFILIATIONS</li><li>CONTACT</li></ul>
</header>

<h1 class="abs hero-title">BUILT RIGHT,</h1>
<div class="abs hero-sub">BUILT TO LAST</div>
<div class="abs btn-estimate">GET AN INSTANT &nbsp;ESTIMATE</div>

<div class="abs quote-shadow"></div>
<form class="abs quote">
  <h3>CALL NOW FOR A FREE QUOTE!</h3>
  <div class="field">Name</div>
  <div class="field">Email</div>
  <div class="field">Subject</div>
  <div class="field msg">Message</div>
  <div class="send">SEND</div>
</form>

<!-- SERVICES -->
<h2 class="abs section-title" style="top:760px;font-size:36px">OUR SERVICES</h2>
<div class="abs service" style="left:160px">
  <div class="ph" style="inset:0;background:linear-gradient(150deg,#8a8e93 0%,#5a5e63 50%,#3e4145 100%)" role="img" aria-label="Photo of a hand measuring roof shingles with a level"></div>
  <div class="label">ROOF INSTALLATION</div>
</div>
<div class="abs service" style="left:610px">
  <div class="ph" style="inset:0;background:linear-gradient(180deg,#d6d8db 0%,#c9cbcf 35%,#c86a45 60%,#a2502f 100%)" role="img" aria-label="Photo of a roofer drilling clay tiles on a roof"></div>
  <div class="label">ROOF REPAIR</div>
</div>

<div class="abs band"></div>
<div class="abs hex" style="left:10px;background:linear-gradient(180deg,#dbeaf7,#a9c9ea 50%,#eef2f6)" role="img" aria-label="Photo of bright windows and skylights"></div>
<div class="abs hex" style="left:310px;background:linear-gradient(160deg,#d8d3c5,#a49e8c 50%,#5f5a4c)" role="img" aria-label="Photo of a roof gutter and downspout"></div>
<div class="abs hex" style="left:610px;background:linear-gradient(170deg,#eef0f2,#c5c9cd 55%,#8f959b)" role="img" aria-label="Photo of grey house siding with a window"></div>
<div class="abs hex" style="left:910px;background:linear-gradient(180deg,#e9eaec,#bfc2c5 60%,#d8d9db)" role="img" aria-label="Photo of a repaired interior kitchen"></div>
<div class="abs hex-label" style="left:-2px">Windows/Skylights</div>
<div class="abs hex-label" style="left:298px">Gutters</div>
<div class="abs hex-label" style="left:597px">Siding</div>
<div class="abs hex-label" style="left:899px">Interior leak damage repairs</div>

<!-- ABOUT -->
<div class="abs about-bg"></div>
<h2 class="abs about-title">About Us</h2>
<p class="abs about-text" lang="en">After over a decade of general contract&shy;ing, we continue to see a repetitive trend by the roof purchase process where homeowners are constantly left confused, nervous, and worried when they need a new roof. As one of the most important features of keeping your home safe, this is unacceptable. Keystone Roofing was created to break this trend.</p>
<div class="ph" style="left:635px;top:1861px;width:402px;height:370px;background:linear-gradient(180deg,#cfe3f4 0%,#e6eef5 40%,#a9b0b8 60%,#a5473d 80%,#8e3b33 100%)" role="img" aria-label="Photo of a city skyline over red tiled rooftops"></div>

<!-- TYPES OF ROOFS -->
<h2 class="abs section-title" style="top:2352px;font-size:28px">TYPES OF ROOFS</h2>
<div class="abs roof" style="left:-103px"><div class="img" style="background:linear-gradient(160deg,#b5845c,#8a5c3c 60%,#6d4a33)" role="img" aria-label="Photo of a cedar shake roof"></div><div class="name" style="text-align:left;padding-left:112px">CEDAR</div></div>
<div class="abs roof" style="left:182px"><div class="img" style="background:linear-gradient(160deg,#cfd4d9,#5f6770 55%,#3f454c)" role="img" aria-label="Photo of a metal roof house"></div><div class="name">METAL</div></div>
<div class="abs roof" style="left:467px"><div class="img" style="background:linear-gradient(160deg,#b7bcc1,#6b6f74 50%,#50504e)" role="img" aria-label="Photo of a slate roof with stone wall"></div><div class="name">SLATE</div></div>
<div class="abs roof" style="left:751px"><div class="img" style="background:linear-gradient(160deg,#e4e8ec,#8a8f95 50%,#5d6166)" role="img" aria-label="Photo of an asphalt shingle roof"></div><div class="name">ASPHALT</div></div>
<div class="abs roof" style="left:1035px"><div class="img" style="background:linear-gradient(180deg,#c9cdd1,#9b5a45 45%,#4e5257 70%)" role="img" aria-label="Photo of a rubber flat roof"></div><div class="name" style="text-align:left;padding-left:104px">RUBBER</div></div>

<!-- RECENT PROJECTS -->
<h2 class="abs section-title" style="top:2743px;font-size:28px">RECENT PROJECTS</h2>
<div class="ph" style="left:21px;top:2828px;width:270px;height:435px;background:linear-gradient(180deg,#565e6c 0%,#6e7686 45%,#3f444d 100%)" role="img" aria-label="Photo of a cupola with weathervane on a new roof"></div>
<div class="abs project-label">Maple Hollow</div>
<div class="ph" style="left:300px;top:2828px;width:430px;height:212px;background:linear-gradient(180deg,#dfe6ee 0%,#8c939b 40%,#b5b1a6 65%,#6f8a52 100%)" role="img" aria-label="Photo of a large grey-shingled home with garages"></div>
<div class="ph" style="left:300px;top:3049px;width:430px;height:214px;background:linear-gradient(180deg,#e6ecf2 0%,#b8c0c8 35%,#8a8f93 60%,#6f8c4f 100%)" role="img" aria-label="Photo of a colonial house with a new roof"></div>
<div class="ph" style="left:737px;top:2828px;width:216px;height:149px;background:linear-gradient(180deg,#d7dde3,#7d848c 55%,#33373c)" role="img" aria-label="Photo of a work truck parked by a house"></div>
<div class="ph" style="left:959px;top:2828px;width:216px;height:149px;background:linear-gradient(180deg,#5f7a47,#e8eaec 45%,#5b6068 80%)" role="img" aria-label="Aerial photo of a white house roof"></div>
<div class="ph" style="left:737px;top:2985px;width:438px;height:278px;background:linear-gradient(180deg,#5d7a44 0%,#7b8290 35%,#e3e5e7 60%,#53575c 100%)" role="img" aria-label="Aerial photo of a large white home with a new roof"></div>

<!-- INSTANT ESTIMATE -->
<div class="abs estimate-bg"></div>
<h2 class="abs section-title" style="top:3360px;font-size:17px;letter-spacing:1px">INSTANT ESTIMATE</h2>
<div class="abs step active" style="left:215px"><b>1</b>PRODUCT SELECTION</div>
<div class="abs step" style="left:439px"><b>2</b>ABOUT YOUR ROOF</div>
<div class="abs step" style="left:646px"><b>3</b>ROOF CONDITION</div>
<div class="abs step" style="left:843px"><b>4</b>GET YOUR COST</div>
<div class="abs section-title" style="top:3490px;font-size:17px;font-weight:400;letter-spacing:1px">STEP 1: PICK YOUR BRAND &amp; SHINGLE:</div>

<div class="abs product" style="left:-52px"><div class="img" style="background:linear-gradient(135deg,#5c6166,#3d4145)" role="img" aria-label="Grey shingle sample"></div><h4 style="margin-left:-10px">Ridgeline Crest</h4><div class="tier"></div><div class="info" style="margin-left:52px">Info</div><div class="calc" style="margin-left:-40px">Calculate your Cost</div></div>
<div class="abs product" style="left:168px"><div class="img" style="background:linear-gradient(135deg,#8c6a59,#5e4538)" role="img" aria-label="Brown shingle sample"><span class="price">$$$</span></div><h4>Ridgeline Autumn Blend</h4><div class="tier">Better</div><div class="info">View Info</div><div class="calc on">Calculate your Cost</div></div>
<div class="abs product" style="left:388px"><div class="img" style="background:linear-gradient(135deg,#5a6677,#36404c)" role="img" aria-label="Blue-grey shingle sample"><span class="price">$$$</span></div><h4>Ridgeline Crest Plus</h4><div class="tier">Best</div><div class="info">View Info</div><div class="calc">Calculate your Cost</div></div>
<div class="abs product" style="left:607px"><div class="img" style="background:linear-gradient(135deg,#6a6763,#3e3c3a)" role="img" aria-label="Dark shingle sample"><span class="price">$$$</span></div><h4>Stonecrest Vista</h4><div class="tier">Good</div><div class="info">View Info</div><div class="calc">Calculate your Cost</div></div>
<div class="abs product" style="left:826px"><div class="img" style="background:linear-gradient(135deg,#66625e,#3a3836)" role="img" aria-label="Charcoal shingle sample"><span class="price">$$$</span></div><h4>Stonecrest Vista Pro</h4><div class="tier">Better</div><div class="info">View Info</div><div class="calc">Calculate your Cost</div></div>
<div class="abs product" style="left:1045px"><div class="img" style="background:linear-gradient(135deg,#6b5445,#3b2f29)" role="img" aria-label="Brown shingle sample"><span class="price">$$$</span></div><h4>Stonecrest Vista<br>Grand</h4><div class="tier">Best</div><div class="info">View Info</div><div class="calc">Calculate your Cost</div></div>

<!-- HAPPY CLIENTS -->
<h2 class="abs section-title" style="top:3918px;font-size:18px;letter-spacing:1px">HAPPY CLIENTS</h2>
<p class="abs quote-text">"We needed to put a new roof on our house, as well as repair a sagging porch roof. Shingles had been flying off and we had had several leaks. Evan provided a very reasonable estimate - well below some of the other HomePro Directory companies. The work was done very promptly and professionally. A couple of issues that arose were settled to our satisfaction and Evan took full ownership of the situation. It was very clear that customer satisfaction is a priority for this company. I would definitely recommend and hire again."</p>
<div class="abs avatar" style="background:linear-gradient(180deg,#9a8777,#5a4a3f)" role="img" aria-label="Client portrait"></div>
<div class="abs client" style="top:4160px;font-size:12px;color:#555">Dana</div>
<div class="abs client" style="top:4178px;font-size:10px;color:#666;font-style:italic">Brookfield Falls</div>
<svg class="abs" style="left:590px;top:4201px" width="40" height="10"><circle cx="8" cy="5" r="4" fill="#29a8e0"/><circle cx="21" cy="5" r="3.5" fill="none" stroke="#29a8e0"/><circle cx="34" cy="5" r="3.5" fill="none" stroke="#29a8e0"/></svg>

<!-- FOOTER -->
<footer class="abs footer"></footer>
<div class="abs fcol" style="left:161px"><h5>KEYSTONE ROOFING</h5><p>Lorem Ipsum is simply dummy text of the printing and typesetting industry. Lorem Ipsum has been the industry's standard dummy text ever since the 1500s, when</p></div>
<div class="abs fcol" style="left:386px"><h5>Services</h5><ul><li>Roof Installation</li><li>Roof Repair</li><li>Windows/Skylights</li></ul></div>
<div class="abs fcol" style="left:612px"><h5>Follow Us</h5><ul><li>Community Page</li><li>News Feed</li><li>Photo Gallery</li></ul></div>
<div class="abs fcol" style="left:837px"><h5>Contact Info</h5>
  <ul class="contact">
    <li><svg width="11" height="9" viewBox="0 0 22 16"><rect x="0" y="0" width="22" height="16" fill="#fff"/><path d="M0 0l11 8 11-8" fill="none" stroke="#29a8e0" stroke-width="2"/></svg>evan@keystoneroofingco.com</li>
    <li><svg width="11" height="11" viewBox="0 0 24 24"><path fill="#fff" d="M6.6 10.8a15 15 0 0 0 6.6 6.6l2.2-2.2c.3-.3.7-.4 1-.2 1.1.4 2.3.6 3.6.6.6 0 1 .4 1 1V20c0 .6-.4 1-1 1A17 17 0 0 1 3 4c0-.6.4-1 1-1h3.5c.6 0 1 .4 1 1 0 1.3.2 2.5.6 3.6.1.3 0 .7-.2 1z"/></svg>555-014-2290</li>
    <li><svg width="11" height="11" viewBox="0 0 24 24"><circle cx="12" cy="12" r="10" fill="#fff"/><circle cx="12" cy="12" r="4" fill="#29a8e0"/></svg>www.keystoneroofingco.com</li>
  </ul>
</div>
<div class="abs copy"><span>© &nbsp;Copyright 2020 All Right Reserved.</span><span><u>Privacy Statement</u> &nbsp;&nbsp;| &nbsp;&nbsp;Terms Of Use</span></div>

</body>
</html>
```